RLTP Business Card Design

I have a rough idea of the design / layout of the company business card but need help in finalizing the design and quality.

I'm looking for the card to be stand out, but simple, on the front with clear detail on the back with space for some one to write any other detail they need onto the card. The rough draft includes the crinkled graph paper back ground which I quite like for the front.

I will need the card design completed and ready to print in Australian business card standard sizes. This includes detail on all colors, fonts and type faces used as well as copy of the original for editing (inserting other employee details).

I have included the company logo and a rough draft of the card, including the graphic I would like to use for the back ground on the front, I am not sure that the graphic is any good for printing, not the highest res.

Thanks,

Owen

```html
<!DOCTYPE html>
<html lang="en">
<head>
<meta charset="utf-8">
<title>RLTP Business Card</title>
<link rel="stylesheet" href="https://fonts.googleapis.com/css2?family=Arimo:wght@400;700&display=swap">
<style>
  :root {
    --page: #ffffff;
    --teal: #78b3b8;
    --ink: #111111;
    --card-grey: #e4e4e4;
    --label: #7a7a7a;
    --paper-light: #eef1f1;
    --paper-mid: #d6dfe0;
  }
  * { margin: 0; padding: 0; box-sizing: border-box; }
  html, body {
    width: 852px; height: 1200px; overflow: hidden;
    background: var(--page);
    font-family: "Arimo", Arial, sans-serif;
  }
  .canvas { position: relative; width: 852px; height: 1200px; }

  .card { position: absolute; left: 294px; width: 296px; height: 180px; overflow: hidden; }

  /* Front */
  .card--front { top: 407px; }
  .paper-texture {
    position: absolute; inset: 0;
    background: radial-gradient(ellipse at 40% 40%, var(--paper-light), var(--paper-mid));
  }
  .side-bar { position: absolute; top: 52px; width: 13px; height: 85px; background: var(--teal); }
  .side-bar--left { left: 0; }
  .side-bar--right { right: 0; }
  .brand {
    position: absolute; left: 58px; top: 57px; width: 196px;
    color: var(--ink);
  }
  .brand__name {
    display: block; font-weight: 700; font-size: 72px; line-height: 64px;
    letter-spacing: 2px;
  }
  .brand__site {
    display: block; font-weight: 700; font-size: 8.6px; line-height: 10px;
    letter-spacing: 0.1px; white-space: nowrap;
  }

  /* Back */
  .card--back { top: 600px; background: var(--card-grey); }
  .back-brand { position: absolute; left: 13px; top: 10px; color: var(--ink); font-weight: 700; }
  .back-brand__name { display: block; font-size: 20px; line-height: 18px; letter-spacing: 1px; }
  .back-brand__site { display: block; font-size: 3px; line-height: 4px; white-space: nowrap; }
  .back-rule { position: absolute; left: 0; right: 0; top: 35px; height: 5px; background: var(--teal); }
  .name-label {
    position: absolute; left: 13px; top: 51px;
    font-size: 12.5px; color: var(--label); font-weight: 400;
  }
  .contact-list {
    position: absolute; left: 175px; top: 103px; list-style: none;
    font-size: 5.5px; color: var(--label); line-height: 13.5px;
  }
</style>
</head>
<body>
<main class="canvas">
  <section class="card card--front" aria-label="Card front">
    <div class="paper-texture" role="img" aria-label="Crinkled graph paper background"></div>
    <div class="side-bar side-bar--left"></div>
    <div class="side-bar side-bar--right"></div>
    <div class="brand">
      <span class="brand__name">RLTP</span>
      <span class="brand__site">REAL LIVE TECH PRODUCTION .COM.AU</span>
    </div>
  </section>

  <section class="card card--back" aria-label="Card back">
    <div class="back-brand">
      <span class="back-brand__name">RLTP</span>
      <span class="back-brand__site">REAL LIVE TECH PRODUCTION</span>
    </div>
    <div class="back-rule"></div>
    <p class="name-label">NAME:</p>
    <ul class="contact-list">
      <li>ADDRESS:</li>
      <li>TEL:</li>
      <li>EMAIL ID:</li>
    </ul>
  </section>
</main>
</body>
</html>
```